The Seven Gates CD cover and booklet - meditation walks

I have created a CD of five meditation walks for the modern mystic - with a professional voice over and really cool music - to help people find their way back home to their true Self. It is very powerful and life-enhancing. The walks were created on the Canary Island of Lanzarote in Mateo's garden and I have stunning photographs taken by pro-photographer Derek Holbrook to accompany the sleeve notes. The result will be a truly beautiful 12pp CD sleeve note booklet - which will itself be so cleanly laid out people will want to pick it up and play! :-) You can do that for me ... and, of course, you will get a free signed copy of the finished CD ... Gus - The Seven Gates - see http://www.quietharbor-retreat.com/
I will send a CD page layout template, the full text and hi-res images to the selected design partner. I attach sample text docs and lo-res logo.
Extra guaranteed money and extended deadline with helpful files.
Hi there - I'm very excited about what designs I get for The Seven Gates CD. Everything is ready to go!
Gus
Today I have uploaded a hi-res version of The Seven Gates logo which you may find helpful.
Gus
Several designers have requested hi-res images of the pictures on the PDF sample pages - so I have uploaded this evening some additional hi-res images as well as a hi-res logo.
hi all you lovely designers! Today is the last day for submission of designs - so if you want a shout ... its now or never. :-)
Photographer

```html
<!DOCTYPE html>
<html lang="en">
<head>
<meta charset="utf-8">
<title>The Seven Gates – walking meditations</title>
<link rel="stylesheet" href="https://fonts.googleapis.com/css2?family=Sacramento&family=Libre+Baskerville:ital,wght@0,400;0,700;1,400;1,700&display=swap">
<style>
  :root{
    --backdrop:#c9cdcd;
    --sea-deep:#1f7f9a;
    --sea-light:#7cc6d4;
    --foam:#e9f1f1;
    --sand-light:#d7c3a8;
    --sand-dark:#a98a6c;
    --cream:#f6efe6;
    --brown:#5a3422;
    --green:#14a54f;
    --navy:#0d2160;
    --teal:#2bb3b1;
    --teal-dark:#16908f;
    --teal-panel:rgba(70,190,188,.82);
    --spine:#7fcdc6;
    --white:#ffffff;
  }
  *{box-sizing:border-box;margin:0;padding:0}
  html,body{width:1200px;height:800px;overflow:hidden}
  body{background:var(--backdrop);position:relative;font-family:"Libre Baskerville",Georgia,serif}

  .front-spine{position:absolute;left:62px;top:78px;width:71px;height:562px;background:var(--spine)}
  .front-cover{position:absolute;left:133px;top:78px;width:572px;height:562px;overflow:hidden}
  .beach-photo{position:absolute;inset:0;
    background:linear-gradient(180deg,var(--sea-deep) 0%,var(--sea-light) 22%,var(--foam) 34%,var(--foam) 40%,var(--sand-light) 50%,var(--sand-dark) 100%)}
  .brand{position:absolute;left:218px;top:18px;display:flex;align-items:center;gap:10px}
  .brand-mark{width:22px;height:22px;background:var(--navy)}
  .brand-name{font-family:"Libre Baskerville",serif;font-weight:700;font-size:18px;color:var(--navy)}

  .cover-title{position:absolute;inset:0;font-family:"Sacramento",cursive;font-weight:400;color:var(--cream);line-height:1}
  .cover-title span{position:absolute;white-space:nowrap}
  .cover-title .name{left:30px;top:248px;font-size:86px}
  .cover-title .sub{left:40px;top:319px;font-size:62px}
  .cover-title .tag{left:150px;top:378px;font-size:42px}
  .cover-title .credit{left:150px;top:429px;font-size:26px;color:var(--brown)}

  .quote-band{position:absolute;left:12px;top:502px;width:550px;height:44px;background:var(--green);color:var(--white);text-align:center;padding-top:5px}
  .quote-band q{display:block;font-weight:700;font-style:italic;font-size:13px;letter-spacing:.3px}
  .quote-band cite{display:block;font-size:11px;font-weight:700;margin-top:2px}

  .back-tray{position:absolute;left:650px;top:265px;width:500px;height:445px;overflow:hidden}
  .water-photo{position:absolute;inset:0;background:linear-gradient(90deg,var(--teal-dark),var(--teal) 40%,var(--sea-light))}
  .back-panel{position:absolute;left:160px;top:0;width:298px;height:445px;background:var(--teal-panel);color:var(--white)}
  .back-spine{position:absolute;right:0;top:0;width:42px;height:445px;background:var(--spine)}
  .back-title{font-family:"Sacramento",cursive;font-weight:400;text-align:center;line-height:1;margin-top:26px}
  .back-title .name{display:block;font-size:42px}
  .back-title .sub{display:block;font-size:27px;margin-top:-8px}
  .tracklist{list-style:none;margin:20px 12px 0 18px;font-size:12px;font-weight:700;letter-spacing:.5px}
  .tracklist li{display:flex;justify-content:space-between;height:26.5px}
  .tracklist .time{font-style:italic;font-weight:400}
  .back-quote{text-align:center;margin-top:16px;font-size:10px}
  .back-quote cite{display:block;font-size:9px;font-style:italic}
  .back-notes{text-align:center;font-size:9px;line-height:1.45;margin:18px 12px 0}
</style>
</head>
<body>
  <div class="front-spine"></div>
  <section class="front-cover">
    <div class="beach-photo" role="img" aria-label="Photo of a sandy beach with waves and a trail of footprints"></div>
    <div class="brand"><span class="brand-mark"></span><span class="brand-name">The Seven Gates</span></div>
    <h1 class="cover-title">
      <span class="name">theSevenGates</span>
      <span class="sub">walking meditations</span>
      <span class="tag">for the mystic in you</span>
      <span class="credit">created by Gus Harrowby</span>
    </h1>
    <div class="quote-band">
      <q>You find out what you’ve been searching for you already are</q>
      <cite>{Ray Calloway}</cite>
    </div>
  </section>

  <section class="back-tray">
    <div class="water-photo" role="img" aria-label="Photo of clear turquoise water with stepping stones"></div>
    <div class="back-panel">
      <h2 class="back-title"><span class="name">theSevenGates</span><span class="sub">walking meditations</span></h2>
      <ol class="tracklist">
        <li><span>Introduction</span><span class="time">{03:52}</span></li>
        <li><span>Via Positiva</span><span class="time">{09:04}</span></li>
        <li><span>Via Negativa</span><span class="time">{06:54}</span></li>
        <li><span>Via Creativa</span><span class="time">{06:22}</span></li>
        <li><span>Via Transformativa</span><span class="time">{05:52}</span></li>
        <li><span>Via Intregativa</span><span class="time">{04:53}</span></li>
      </ol>
      <p class="back-quote">“What you are looking for is what is looking”<cite>{Brother Anselm}</cite></p>
      <p class="back-notes">These walking meditations are created in Mateo’s garden Lanzarote will make you feel grounded and uplifted, centered and expansive, connected with your deepest purpose and true Self</p>
    </div>
    <div class="back-spine"></div>
  </section>
</body>
</html>
```